Business & Good Life in perfect harmony

Our company is engage in event planning & services , we have Convention center ideal for seminars, retreats,conventions, conferences or even concerts & also offers lodging facilities particularly of "ON - LINE ROOM RESERVATIONS /ACCOMMODATIONS "
Also we have Clubhouse & restobar , an elegant venue ideal for weddings, birthday celebration, parties & other memorable gatherings, as well as sports activities.
Target Market(s)
Travellers
Event Organizers
Conference / seminar Coordinators
Industry/Entity Type
Event Planning
Contact Information for Business Card
Lia R. Montero , Sales & Operation Manager
Bluecrest Business & Convention Center Corp.
/ Bluecrest Clubhouse & Restobar
Contact #s : 082-5913026 ; 0917 4356128
Website : www. bluecrestplaza.example
Email add : bluecrest.lia.plaza@mailbox.example
bluecrest.plaza@inbox.example
Facebook : Bluecrest Plaza

```html
<!DOCTYPE html>
<html lang="en">
<head>
<meta charset="utf-8">
<title>Lia R. Montero – Business Card</title>
<link rel="stylesheet" href="https://fonts.googleapis.com/css2?family=Yellowtail&family=Questrial&display=swap">
<style>
  :root {
    --navy: #123a73;
    --navy-deep: #0d2f62;
    --white: #ffffff;
    --sky-light: #e3f2fd;
    --sky-mid: #8fcaf3;
    --sky-deep: #3f95dc;
  }
  html, body {
    margin: 0;
    padding: 0;
    overflow: hidden;
    background: var(--white);
  }
  .card {
    position: relative;
    width: 1200px;
    height: 686px;
    overflow: hidden;
    font-family: "Questrial", "Century Gothic", sans-serif;
    color: var(--white);
  }
  .card__backdrop {
    position: absolute;
    inset: 0;
    background:
      radial-gradient(circle at 88% 8%, var(--sky-light) 0%, rgba(227,242,253,0) 45%),
      linear-gradient(200deg, var(--sky-mid) 0%, var(--sky-deep) 55%, var(--sky-mid) 100%);
  }
  .card__panel {
    position: absolute;
    inset: 0;
    width: 1200px;
    height: 686px;
  }
  .name {
    position: absolute;
    left: 130px;
    top: 40px;
    margin: 0;
    font-family: "Yellowtail", cursive;
    font-weight: 400;
    font-size: 110px;
    line-height: 1;
    letter-spacing: 1px;
  }
  .role {
    position: absolute;
    left: 100px;
    top: 204px;
    margin: 0;
    font-size: 22px;
    line-height: 29px;
  }
  .contacts {
    position: absolute;
    left: 126px;
    top: 336px;
    margin: 0;
    padding: 0;
    list-style: none;
    font-size: 28px;
    line-height: 34px;
  }
  .contact {
    display: flex;
    align-items: flex-start;
  }
  .contact__icon {
    flex: 0 0 auto;
    width: 46px;
    height: 34px;
  }
  .contact--phone { margin-bottom: 22px; }
  .contact--email { margin-bottom: 28px; }
  .contact--web { margin-bottom: 38px; }
  .contact__text { padding-left: 4px; }
</style>
</head>
<body>
  <div class="card">
    <div class="card__backdrop" role="img" aria-label="Faceted light blue geometric background"></div>

    <svg class="card__panel" viewBox="0 0 1200 686" aria-hidden="true">
      <path d="M0 0 H812 C885 110 905 300 865 460 C835 570 770 640 712 686 H0 Z"
            fill="var(--navy)" stroke="var(--white)" stroke-width="10"/>
    </svg>

    <h1 class="name">Lia R. Montero</h1>
    <p class="role">Sales &amp; Operation Manager Bluecrest Business &amp;<br>Convention Center Corp. / Bluecrest Clubhouse &amp; Restobar</p>

    <ul class="contacts">
      <li class="contact contact--phone">
        <svg class="contact__icon" viewBox="0 0 46 34" aria-hidden="true">
          <circle cx="18" cy="17" r="15" fill="none" stroke="var(--white)" stroke-width="3"/>
          <path d="M12 9 l4 -1 l2 5 l-3 2 c1 3 3 5 6 6 l2 -3 l5 2 l-1 4 c-8 1 -16 -7 -15 -15 z" fill="var(--white)"/>
        </svg>
        <span class="contact__text">: 082-5913026 / 0917 4356128</span>
      </li>
      <li class="contact contact--email">
        <svg class="contact__icon" viewBox="0 0 46 34" aria-hidden="true">
          <rect x="3" y="8" width="34" height="20" rx="3" fill="var(--white)"/>
          <path d="M5 10 L20 21 L35 10" fill="none" stroke="var(--navy)" stroke-width="2.5"/>
        </svg>
        <span class="contact__text">: bluecrest.lia.plaza@mailbox.example<br>&nbsp;&nbsp;bluecrest.plaza@inbox.example</span>
      </li>
      <li class="contact contact--web">
        <svg class="contact__icon" viewBox="0 0 46 34" aria-hidden="true">
          <rect x="6" y="3" width="28" height="28" rx="3" fill="var(--white)"/>
        </svg>
        <span class="contact__text">: www. bluecrestplaza.example</span>
      </li>
      <li class="contact contact--social">
        <svg class="contact__icon" viewBox="0 0 46 34" aria-hidden="true">
          <circle cx="20" cy="17" r="15" fill="var(--white)"/>
        </svg>
        <span class="contact__text">: Bluecrest Plaza</span>
      </li>
    </ul>
  </div>
</body>
</html>
```